8"x5" postcard for Wireless Internet introduction to new mountain town market

I need to market high speed internet to a resort mountain town without doing the obvious laptop on a mountain top thing, so tired. We are going to be competing directly with another provider with same cost, but we will be offering free installation. The area is Aspen Colorado, so the clientele are outdoor types who have suffered for years from being disconnected in their mountain town. We offer fast internet and excellent customer service from people who live in their neck of the woods.

Target Market(s)

23-55 years old, both resort living, families and ski bums

Font styles to use
Sans Serif

Colors

Designer to choose colors to be used in the design.

Requirements
Must have
• Visual appeal and fresh verbiage. We don't mind being a little edgy. We are a young company and we want to appeal to people looking for a provider who gets them. We prefer a clean look.
Nice to have
• Nice to have colors that match our logo
Should not have
• stuffy concepts or verbiage that is too much like a car salesman. We don't want to look like a 'big box' company.

```html
<!DOCTYPE html>
<html lang="en">
<head>
<meta charset="utf-8">
<title>Summit Signal Postcard</title>
<link rel="stylesheet" href="https://fonts.googleapis.com/css2?family=Oswald:wght@400;500;600&display=swap">
<style>
  :root {
    --page-bg: #b9b9b9;
    --card-white: #ffffff;
    --ink: #111111;
    --signal-orange: #f9a41a;
    --band-yellow: #f4e51c;
    --band-orange: #faa324;
    --sky-top: #1f6fc0;
    --sky-mid: #3d9ad6;
    --snow: #dfe6ec;
    --forest: #5b5a2c;
    --autumn: #b8671f;
    --lake: #2a3a48;
    --headline: #ffffff;
  }
  * { margin: 0; padding: 0; box-sizing: border-box; }
  html, body { width: 986px; height: 1200px; overflow: hidden; }
  body {
    background: var(--page-bg);
    font-family: "Oswald", "Arial Narrow", sans-serif;
    color: var(--ink);
    position: relative;
  }
  .postcard {
    position: absolute;
    left: 136px;
    width: 725px;
    height: 454px;
    overflow: hidden;
  }
  .postcard--front { top: 116px; }
  .postcard--back { top: 620px; background: var(--card-white); }

  /* Front */
  .scene {
    position: absolute; inset: 0;
    background: linear-gradient(180deg, var(--sky-top) 0%, var(--sky-mid) 34%, var(--snow) 52%, var(--autumn) 68%, var(--forest) 80%, var(--lake) 88%, var(--lake) 100%);
  }
  .headline {
    position: absolute; top: 14px; left: 0; right: 0;
    text-align: center;
    color: var(--headline);
    font-size: 30px; font-weight: 500;
    letter-spacing: 0.2px;
    transform: scaleX(0.86);
  }
  .signal-icon { position: absolute; left: 265px; top: 106px; }
  .signal-faint { position: absolute; top: 40px; opacity: 0.3; }
  .signal-faint--left { left: 10px; }
  .signal-faint--right { right: 10px; }

  .contact-band {
    position: absolute; left: 0; top: 373px;
    width: 100%; height: 65px;
    background: linear-gradient(90deg, var(--band-yellow), var(--band-orange));
    display: flex; align-items: center;
  }
  .brand {
    display: flex; align-items: center; gap: 8px;
    font-weight: 600; color: var(--ink);
  }
  .brand__dot { width: 34px; height: 34px; border-radius: 50%; background: var(--ink); }
  .brand__name { font-size: 24px; line-height: 1; letter-spacing: 0.5px; white-space: nowrap; }
  .contact-band .brand { margin-left: 32px; }
  .band-divider { position: absolute; left: 255px; top: 14px; width: 2px; height: 38px; background: var(--ink); }
  .band-item {
    position: absolute; top: 0; height: 65px;
    display: flex; align-items: center; gap: 4px;
    font-size: 21px; font-weight: 500;
    white-space: nowrap;
    transform-origin: left center;
    transform: scaleX(0.86);
  }
  .band-item--phone { left: 300px; }
  .band-item--web { left: 505px; }

  /* Back */
  .postcard--back .brand { position: absolute; left: 26px; top: 28px; }
  .postcard--back .brand__dot { background: var(--signal-orange); width: 38px; height: 38px; }
  .postcard--back .brand__name { font-size: 28px; }
  .offer-box {
    position: absolute; left: 25px; top: 104px;
    width: 352px; height: 224px;
    background: linear-gradient(90deg, var(--band-yellow), var(--band-orange));
  }
  .offer-list { list-style: none; position: absolute; left: 10px; top: 24px; }
  .offer-list li {
    position: relative; padding-left: 16px;
    font-size: 27px; font-weight: 500; line-height: 37px;
    margin-bottom: 11px;
    transform-origin: left; transform: scaleX(0.86);
    white-space: nowrap;
  }
  .offer-list li::before {
    content: "›"; position: absolute; left: 0; top: -2px; font-weight: 600;
  }
  .call-now {
    position: absolute; left: 25px; top: 346px;
    font-size: 42px; font-weight: 600; line-height: 1;
    transform-origin: left; transform: scaleX(0.86);
    white-space: nowrap;
  }
  .web-line {
    position: absolute; left: 25px; top: 394px;
    font-size: 16px; font-weight: 500;
    transform-origin: left; transform: scaleX(0.86);
    white-space: nowrap;
  }
  .stamp-box { position: absolute; left: 617px; top: 34px; width: 74px; height: 96px; border: 1.5px solid var(--ink); }
  .address-box { position: absolute; left: 401px; top: 272px; width: 280px; height: 141px; border: 1.5px solid var(--ink); }
</style>
</head>
<body>
  <section class="postcard postcard--front">
    <div class="scene" role="img" aria-label="Photo of a snowy mountain peak above an autumn valley and an alpine lake under a starry blue sky"></div>
    <h1 class="headline">NO MORE suffered from being disconnected in mountain town</h1>

    <svg class="signal-faint signal-faint--left" width="120" height="150" viewBox="0 0 120 150" aria-hidden="true">
      <g fill="none" stroke="#6fb6e0" stroke-width="14" stroke-linecap="round">
        <path d="M20 40 A45 45 0 0 1 20 110"/>
        <path d="M45 15 A80 80 0 0 1 45 135"/>
        <path d="M70 5 A110 110 0 0 1 70 145"/>
      </g>
    </svg>
    <svg class="signal-faint signal-faint--right" width="120" height="150" viewBox="0 0 120 150" aria-hidden="true">
      <g fill="none" stroke="#6fb6e0" stroke-width="14" stroke-linecap="round">
        <path d="M100 40 A45 45 0 0 0 100 110"/>
        <path d="M75 15 A80 80 0 0 0 75 135"/>
        <path d="M50 5 A110 110 0 0 0 50 145"/>
      </g>
    </svg>

    <svg class="signal-icon" width="160" height="120" viewBox="0 0 160 120" aria-hidden="true">
      <g fill="none" stroke="var(--signal-orange)" stroke-width="11" stroke-linecap="round">
        <path d="M62 42 A25 25 0 0 0 62 78"/>
        <path d="M98 42 A25 25 0 0 1 98 78"/>
        <path d="M45 25 A50 50 0 0 0 45 95"/>
        <path d="M115 25 A50 50 0 0 1 115 95"/>
        <path d="M28 8 A75 75 0 0 0 28 112"/>
        <path d="M132 8 A75 75 0 0 1 132 112"/>
      </g>
      <circle cx="80" cy="60" r="11" fill="var(--signal-orange)"/>
    </svg>

    <div class="contact-band">
      <div class="brand"><span class="brand__dot"></span><span class="brand__name">SUMMIT SIGNAL</span></div>
      <span class="band-divider"></span>
      <div class="band-item band-item--phone">
        <svg width="20" height="20" viewBox="0 0 24 24" aria-hidden="true"><path fill="#111" d="M6.6 10.8a15.1 15.1 0 0 0 6.6 6.6l2.2-2.2a1 1 0 0 1 1-.25 11.4 11.4 0 0 0 3.6.57 1 1 0 0 1 1 1V20a1 1 0 0 1-1 1A17 17 0 0 1 3 4a1 1 0 0 1 1-1h3.5a1 1 0 0 1 1 1c0 1.25.2 2.45.57 3.6a1 1 0 0 1-.25 1z"/></svg>
        <span>CALL NOW! 555.014.2277</span>
      </div>
      <div class="band-item band-item--web">
        <svg width="22" height="22" viewBox="0 0 24 24" aria-hidden="true"><circle cx="12" cy="12" r="10" fill="none" stroke="#111" stroke-width="2"/><path d="M2 12h20M12 2c3 3 3 17 0 20M12 2c-3 3-3 17 0 20" fill="none" stroke="#111" stroke-width="1.5"/></svg>
        <span>www.summitsignal.net</span>
      </div>
    </div>
  </section>

  <section class="postcard postcard--back">
    <div class="brand"><span class="brand__dot"></span><span class="brand__name">SUMMIT SIGNAL</span></div>
    <div class="offer-box">
      <ul class="offer-list">
        <li>10, 25 AND 40MBPS SPEEDS</li>
        <li>PRICES START AT $59.95</li>
        <li>TAKE ADVANTAGE OF OUR FREE<br>RESIDENTIAL INSTALL PROMOTION!</li>
      </ul>
    </div>
    <p class="call-now">CALL NOW! 555.014.2277</p>
    <p class="web-line">www.summitsignal.net &nbsp;|&nbsp; hello@summitsignal.net</p>
    <div class="stamp-box"></div>
    <div class="address-box"></div>
  </section>
</body>
</html>
```